Flyer Design Project

We are a storm restoration company that has recently begun restoration from water/flood damage from Hurricane Sandy. We provide disaster relief to homeowners and or commercial property owners after a flood. To start we offer cleanup and remediation which is taking out and disposing of all wet items in a home or business and the cutting out of walls, flooring and other items affected by a flood. We then provide remediation which includes the drying out of a home or business along with a dehumidifier to take all the moisture out of the air and to put it simply dry out the home. We also uses chemicals to clean and provide mold remediation to prevent to growth of mold. We work directly with a customers insurance company if they have flood insurance and after that we provide the services to rebuild and bring their property back to its condition before the storm.

Im looking for an informational type flier that I could insert into our business folders that we give to customers and also to use as fliers to pass out to potential customers. I want potential customers to look at this and feel comfortable with calling my company and working with us.

Company name Bellridge Building Partners. I attached our company logo.

Target Market(s)

Those affected by flooding from Hurricane Sandy

Industry/Entity Type

Insurance

Requirements
Must have
• Company logo, name and colors on flier
Nice to have
• Color photos that have to do with water restoration or showing flood damamge

```html
<!DOCTYPE html>
<html lang="en">
<head>
<meta charset="utf-8">
<title>Bellridge Building Partners – Water Restoration Flyer</title>
<link href="https://fonts.googleapis.com/css2?family=Libre+Franklin:wght@700;800&display=swap" rel="stylesheet">
<style>
  :root {
    --page: #ffffff;
    --sun: #fcc92c;
    --navy: #1f2a5a;
    --white: #ffffff;
    --wall-top: #cfc3a4;
    --wall-mid: #b3a27a;
    --water-line: #3b3022;
    --floor: #b89c5c;
    --floor-low: #d0b572;
  }
  * { box-sizing: border-box; margin: 0; padding: 0; }
  html, body { width: 939px; height: 1200px; overflow: hidden; background: var(--page); }
  .flyer {
    position: relative;
    width: 939px;
    height: 1200px;
    font-family: "Libre Franklin", "Arial", sans-serif;
    color: var(--white);
  }
  .flyer__photo {
    position: absolute;
    left: 0; top: 0;
    width: 939px; height: 690px;
    background: linear-gradient(180deg,
      var(--wall-top) 0%,
      var(--wall-mid) 38%,
      #8a7650 52%,
      var(--water-line) 58%,
      #6b5834 64%,
      var(--floor) 76%,
      var(--floor-low) 100%);
  }
  .flyer__panel {
    position: absolute;
    left: 0; top: 690px;
    width: 939px; height: 510px;
    background: var(--sun);
  }
  .service-call {
    position: absolute;
    right: 64px;
    top: 150px;
    text-align: right;
    font-weight: 800;
    line-height: 1;
    text-shadow: 0 1px 2px rgba(0,0,0,.25);
  }
  .service-call__hours { font-size: 42px; }
  .service-call__label { font-size: 27px; margin-top: 4px; }
  .service-call__prompt { font-size: 27px; margin-top: 42px; }
  .service-call__number { font-size: 46px; margin-top: 4px; letter-spacing: 1px; }
  .headline {
    position: absolute;
    left: 68px;
    top: 448px;
    font-size: 38px;
    font-weight: 800;
    line-height: 52px;
    text-transform: uppercase;
    text-shadow: 0 1px 2px rgba(0,0,0,.3);
  }
  .brand {
    position: absolute;
    left: 70px;
    top: 930px;
    display: flex;
    align-items: center;
    gap: 16px;
    color: var(--navy);
    font-weight: 800;
    font-size: 34px;
    line-height: 1.05;
  }
  .brand__mark {
    width: 36px; height: 36px;
    border-radius: 50%;
    background: var(--navy);
    flex: none;
  }
  .services {
    position: absolute;
    left: 466px;
    top: 712px;
    width: 410px;
    font-size: 13.6px;
    font-weight: 700;
    line-height: 1.36;
    text-align: justify;
  }
</style>
</head>
<body>
  <main class="flyer">
    <div class="flyer__photo" role="img" aria-label="Photo of a flood-damaged basement with a concrete wall, dark water line and muddy floor"></div>
    <div class="flyer__panel"></div>

    <div class="service-call">
      <div class="service-call__hours">24/7</div>
      <div class="service-call__label">SERVICE</div>
      <div class="service-call__prompt">PLEASE CALL</div>
      <div class="service-call__number">+1 000 000</div>
    </div>

    <h1 class="headline">Solution for<br>water restoration<br>and<br>flood damage</h1>

    <div class="brand">
      <span class="brand__mark"></span>
      <span class="brand__name">Bellridge<br>Building Partners</span>
    </div>

    <div class="services">
      <p>We provide disaster relief to homeowners and or commercial property owners after a flood.</p>
      <p>To start we offer cleanup and remediation which is taking out and disposing of all wet items in a home or business and the cutting out of walls, flooring and other items affected by a flood.</p>
      <p>We then provide remediation which includes the drying out of a home or business along with a dehumidifier to take all the moisture out of the air and to put it simply dry out the home.</p>
      <p>We also uses chemicals to clean and provide mold remediation to prevent to growth of mold.</p>
      <p>We work directly with a customers insurance company if they have flood insurance and after that we provide the services to rebuild and bring their property back to its condition before the storm.</p>
    </div>
  </main>
</body>
</html>
```